Flyer for Beacon Ledger & Returns, a local tax practice

Flyer for my business to be distributed locally in the Western Suburb of Melbourne (Size: DL, Fold: Flat, Backside: Blank) This will include below information (Font, color and capitalization of the text is for the designer's creativity):
Beacon Ledger & Returns Your Local Tax Accountant
ABN: 71 284 519 036
Address: 9 Mirra Close, Tarwin Heights
dovpelk@blrau.com.au
Call Florin on 0417 865 209 to book your appointment
Services we offer:
Individual & Company Tax Returns
Company & Trust formation
Business Advisory
Bookkeeping
BAS & IAS
Payroll
TPAR
Please include the logo of the business attached which was designed by ArtHarbor few years ago.
Please include the Vendrio, WRD and Pulva logos somewhere in the bottom, preferable the same size and aligned (attached)

```html
<!DOCTYPE html>
<html lang="en">
<head>
<meta charset="utf-8">
<title>Beacon Ledger &amp; Returns – Flyer</title>
<link href="https://fonts.googleapis.com/css2?family=Montserrat:wght@400;500;600;700;800&display=swap" rel="stylesheet">
<style>
  :root {
    --orange: #e8541f;
    --orange-light: #f07a34;
    --charcoal: #262626;
    --grey-line: #c9c9c9;
    --white: #ffffff;
    --ink: #1d1d1d;
    --teal: #1e7fa6;
    --sky: #27a9e1;
    --partner-plum: #6a3a8c;
    --seal-fill: #b9c2b0;
  }
  * { margin: 0; padding: 0; box-sizing: border-box; }
  html, body { width: 725px; height: 1200px; overflow: hidden; background: #e6e6e6; }
  body { font-family: "Montserrat", sans-serif; }
  .flyer { position: relative; width: 725px; height: 1200px; background: var(--white); overflow: hidden; }

  .hero-photo {
    position: absolute; left: 0; top: 0; width: 725px; height: 340px;
    background: linear-gradient(160deg, #dfe3e8 0%, #c8ccd1 35%, #eceef0 60%, #d9c2ad 100%);
  }
  .wave-layer { position: absolute; left: 0; top: 0; }

  .brand { position: absolute; left: 318px; top: 378px; display: flex; align-items: center; gap: 12px; white-space: nowrap; }
  .brand-square { width: 28px; height: 28px; background: var(--charcoal); flex: none; }
  .brand-name { font-weight: 700; font-size: 22px; color: var(--orange); letter-spacing: 0.2px; }

  .headline {
    position: absolute; left: 50px; top: 512px; color: var(--white);
    font-weight: 800; font-size: 33px; line-height: 40px; white-space: nowrap;
  }
  .headline .light { font-weight: 500; }
  .headline-rule { position: absolute; left: 50px; top: 646px; width: 290px; height: 3px; background: var(--white); opacity: 0.85; }

  .services-pill {
    position: absolute; left: 26px; top: 670px; width: 326px; height: 38px;
    background: var(--white); border-radius: 19px;
    font-weight: 600; font-size: 24px; color: var(--ink);
    padding-left: 22px; line-height: 38px;
  }

  .service-list { position: absolute; list-style: none; color: var(--white); font-weight: 500; font-size: 21px; line-height: 24px; }
  .service-list.left { left: 50px; top: 730px; width: 340px; }
  .service-list.right { left: 434px; top: 734px; width: 260px; }
  .service-list li { position: relative; padding-left: 46px; }
  .service-list.left li { margin-bottom: 18px; }
  .service-list.right li { margin-bottom: 16px; }
  .service-list li::before {
    content: ""; position: absolute; left: 0; top: 0; width: 24px; height: 24px;
    border-radius: 50%; background: var(--white); box-shadow: inset 0 0 0 6px #f6d5c6;
  }
  .service-list .tick::before { background: var(--white); box-shadow: none; }
  .service-list .tick svg { position: absolute; left: 5px; top: 6px; }
  .spine { position: absolute; width: 2px; background: rgba(255,255,255,0.7); }
  .spine.left { left: 61px; top: 754px; height: 110px; }
  .spine.right { left: 445px; top: 758px; height: 110px; }

  .partners { position: absolute; left: 0; top: 898px; width: 725px; height: 117px; background: var(--white); }
  .partner-pulva { position: absolute; left: 70px; top: 24px; display: flex; align-items: center; gap: 10px; }
  .partner-pulva .name { font-weight: 700; font-size: 28px; color: var(--sky); }
  .partner-pulva .badge { width: 72px; height: 72px; border-radius: 50%; background: var(--teal); }
  .divider { position: absolute; top: 20px; width: 2px; height: 70px; background: #9a9a9a; }
  .divider.one { left: 272px; }
  .divider.two { left: 460px; }
  .partner-wrd { position: absolute; left: 318px; top: 14px; width: 100px; text-align: center; }
  .partner-wrd .seal { width: 70px; height: 70px; margin: 0 auto; border-radius: 50%; background: var(--seal-fill); }
  .partner-wrd .agent { font-size: 8px; font-weight: 500; color: var(--ink); margin-top: 4px; line-height: 10px; }
  .partner-vendrio { position: absolute; left: 500px; top: 38px; display: flex; align-items: center; gap: 10px; }
  .partner-vendrio .mark { width: 36px; height: 36px; border-radius: 50%; background: var(--partner-plum); }
  .partner-vendrio .name { font-weight: 700; font-size: 26px; color: var(--partner-plum); }

  .contact-band { position: absolute; left: 0; top: 1015px; }
  .call-line { position: absolute; left: 58px; top: 1026px; color: var(--white); font-weight: 500; font-size: 21px; line-height: 28px; white-space: nowrap; }
  .call-line strong { color: var(--charcoal); font-weight: 800; font-size: 24px; }
  .call-line .phone-icon { position: absolute; left: -26px; top: 5px; }
  .details { position: absolute; left: 52px; top: 1103px; list-style: none; color: var(--white); font-size: 18px; font-weight: 500; line-height: 28px; white-space: nowrap; }
  .details li { position: relative; padding-left: 36px; }
  .details li::before { content: ""; position: absolute; left: 0; top: 7px; width: 14px; height: 14px; border-radius: 50%; background: var(--orange-light); }
</style>
</head>
<body>
<main class="flyer">
  <div class="hero-photo" role="img" aria-label="Photo of a hand using a calculator beside a laptop, a pen and printed financial statements"></div>

  <svg class="wave-layer" width="725" height="900" viewBox="0 0 725 900" aria-hidden="true">
    <defs>
      <linearGradient id="orangeFill" x1="0" y1="0" x2="1" y2="1">
        <stop offset="0" stop-color="#e8541f"/>
        <stop offset="1" stop-color="#e24a1a"/>
      </linearGradient>
    </defs>
    <path d="M0,260 C220,300 470,330 725,290 L725,900 L0,900 Z" fill="#ffffff"/>
    <path d="M0,255 C120,270 250,320 360,400 C460,470 600,482 725,470 L725,515 C560,540 420,512 300,472 C200,442 100,428 0,432 Z" fill="#262626"/>
    <path d="M0,440 C130,432 260,458 390,505 C520,548 640,548 725,530" fill="none" stroke="#c9c9c9" stroke-width="6"/>
    <path d="M0,452 C140,442 280,482 420,522 C560,560 650,546 725,530 L725,900 L0,900 Z" fill="url(#orangeFill)"/>
  </svg>

  <div class="brand">
    <span class="brand-square"></span>
    <span class="brand-name">Beacon Ledger &amp; Returns</span>
  </div>

  <h1 class="headline">Beacon Ledger<br>&amp; Returns <span class="light">Your Local</span><br>Tax Accountant</h1>
  <div class="headline-rule"></div>

  <div class="services-pill">Services we offer:</div>

  <div class="spine left"></div>
  <ul class="service-list left">
    <li>Individual &amp; company<br>tax returns</li>
    <li>Company &amp; trust<br>formation</li>
    <li>Business advisory</li>
  </ul>

  <div class="spine right"></div>
  <ul class="service-list right">
    <li>Bookkeeping</li>
    <li>Bas &amp; ias</li>
    <li>Payroll</li>
    <li class="tick"><svg width="14" height="12" viewBox="0 0 14 12"><path d="M1,6 L5,10 L13,1" fill="none" stroke="#262626" stroke-width="2.5"/></svg>Tpar</li>
  </ul>

  <section class="partners">
    <div class="partner-pulva"><span class="name">Pulva</span><span class="badge"></span></div>
    <div class="divider one"></div>
    <div class="partner-wrd">
      <div class="seal"></div>
      <p class="agent">Tax Agent<br>26508147</p>
    </div>
    <div class="divider two"></div>
    <div class="partner-vendrio"><span class="mark"></span><span class="name">Vendrio</span></div>
  </section>

  <svg class="contact-band" width="725" height="185" viewBox="0 0 725 185" aria-hidden="true">
    <polygon points="0,0 585,0 675,110 725,110 725,185 0,185" fill="#e8541f"/>
    <polygon points="0,75 535,75 645,185 0,185" fill="#262626"/>
    <polygon points="590,110 725,110 725,185 660,185" fill="#f07a34"/>
  </svg>

  <p class="call-line">
    <svg class="phone-icon" width="18" height="18" viewBox="0 0 18 18"><circle cx="9" cy="9" r="9" fill="#f8c8b2"/><path d="M6,4 L8,7 L7,8 C8,10 9,11 10,11 L11,10 L14,12 L13,14 C9,14 4,9 4,5 Z" fill="#e8541f"/></svg>
    Call Florin on <strong>0417 865 209</strong><br>to book your appointment
  </p>

  <ul class="details">
    <li>ABN: 71 284 519 036</li>
    <li>9 Mirra Close, Tarwin Heights</li>
    <li>dovpelk@blrau.com.au</li>
  </ul>
</main>
</body>
</html>
```